Professional PowerPoint Template for Data Reports, Presentations

We are a small leadership coaching/consulting firm and would like to update our PowerPoint template that we use with our clients, who are typically mid-senior level company professionals. I've attached a sample Powerpoint as well as our branding guide. The cover page is what needs the most work - just doesn't look current/professional enough. We do want to keep the pages after that clean, with come color but enough space for text and graphics.
Target Market(s)
Senior mgmt and HR executives in small-mid sized companies
Font styles to use
Sans Serif
Requirements
Must have
- Professional
- Clean
- Tied to company color scheme/logo
Nice to have
- Our title pages don't usually have many words on them; we'd like a design that has a lot of color - probably still using mainly our blue but accented with other colors.
- Need simple but smart looking pages after cover with lot of space; mostly we have text on the slides. Currently this is often in bullet point style, but we could probably upgrade the options there.
Should not have
- Anything that looks like a marketing style, as we typically use these with our current clients to share results of data collected, project plans, etc.

```html
<!DOCTYPE html>
<html lang="en">
<head>
<meta charset="utf-8">
<title>Harborline Presentation Template</title>
<link href="https://fonts.googleapis.com/css2?family=Montserrat:wght@600;700&family=Open+Sans:wght@400;600&display=swap" rel="stylesheet">
<style>
:root{
  --stage:#a9a7a7;
  --blue:#2c5b95;
  --blue-deep:#234e86;
  --navy:#1d3d66;
  --teal:#6db5a6;
  --orange:#ef8450;
  --lavender:#e9e7f2;
  --ink:#2a4f80;
  --text:#3a3a3a;
  --white:#ffffff;
}
*{box-sizing:border-box;margin:0;padding:0}
html,body{width:1200px;height:1200px;overflow:hidden;background:var(--stage)}
.deck{
  width:1200px;height:1200px;padding:28px 18px;
  display:grid;grid-template-columns:repeat(4,280px);grid-auto-rows:210px;
  column-gap:14.6px;row-gap:27px;
}
.slide{position:relative;width:280px;height:210px;overflow:hidden;background:var(--white);
  font-family:"Open Sans",sans-serif;color:var(--text)}
.h{font-family:"Montserrat",sans-serif;font-weight:700;text-transform:uppercase;letter-spacing:.2px}
.title{position:absolute;left:14px;top:10px;font-size:8.5px;color:var(--ink)}
.body{font-size:4.7px;line-height:1.55}
.abs{position:absolute}
.photo-city{background:linear-gradient(180deg,rgba(255,255,255,0) 15%,rgba(140,170,210,.22) 45%,rgba(30,60,110,.15) 75%,rgba(255,255,255,0))}
.photo-room-blue{background:linear-gradient(180deg,#b7c3e6 0%,#7e8fc4 40%,#2e3d63 75%,#5b6ea3 100%)}
.photo-room-warm{background:linear-gradient(180deg,#e9e3df 0%,#d8cfc8 35%,#6a5445 60%,#a99383 100%)}
.cover{background:linear-gradient(180deg,#2d5d98,#22508a)}
.cover .brand{position:absolute;right:14px;top:13px;color:var(--white);font-family:"Montserrat",sans-serif;
  font-weight:600;font-size:12.5px;letter-spacing:2.4px}
.cover-title{position:absolute;color:var(--white);font-size:8.8px;line-height:1.65;text-align:right}
.ring{position:absolute;border-radius:50%;border-style:solid;border-color:var(--white)}
.band{position:absolute;left:40px;right:0;top:69px;height:74px}
.foot{position:absolute;left:8px;right:8px;bottom:3px;height:7px;background:var(--blue);
  display:flex;align-items:center;justify-content:space-between;padding-left:4px;color:var(--white);font-size:4.3px}
.foot-brand{display:flex;align-items:center;gap:2px;font-family:"Montserrat",sans-serif;font-weight:600;letter-spacing:.6px}
.foot-brand::before{content:"";width:4px;height:4px;border-radius:50%;background:var(--white)}
.foot-page{width:18px;height:100%;background:var(--orange);text-align:center;font-size:3.6px;line-height:7px}
.foot-sign{position:absolute;right:8px;bottom:5px;display:flex;align-items:center;gap:4px;color:var(--white);
  font-family:"Montserrat",sans-serif;font-weight:600;font-size:6px;letter-spacing:1.2px}
.foot-sign .pill{width:16px;height:7px;border-radius:4px;background:var(--blue);font-size:3.6px;text-align:center;line-height:7px;letter-spacing:0}
.toc-item{position:absolute;display:flex;gap:5px;align-items:flex-start}
.toc-num{font-size:13px;line-height:1;font-weight:400}
.toc-item .lbl{font-size:4.8px;line-height:1.45}
.dot{position:absolute;border-radius:50%;display:flex;align-items:center;justify-content:center}
.dot svg{width:55%;height:55%}
.svc{position:absolute;display:flex;gap:5px;width:115px}
.svc .ic{flex:0 0 14px;height:14px;border-radius:50%;display:flex;align-items:center;justify-content:center}
.svc .ic svg{width:8px;height:8px}
.svc .nm{font-size:5.6px;margin-bottom:2px}
.svc .ds{font-size:3.9px;line-height:1.5}
.card{position:absolute;width:100px;height:66px;background:linear-gradient(180deg,#e3e3e6,#cfd0d5);
  text-align:center;padding:6px 7px;font-size:3.9px;line-height:1.5}
.card .nm{font-size:5px;color:var(--ink);margin:3px 0 2px}
.diff .k{font-size:5px;color:var(--orange);margin-bottom:2px;text-transform:uppercase}
.diff .ds{font-size:3.9px;line-height:1.5;margin-bottom:7px}
.circle{position:absolute;border-radius:50%;mix-blend-mode:multiply}
</style>
</head>
<body>
<main class="deck">

<section class="slide cover">
  <div class="abs photo-city" style="inset:0" role="img" aria-label="Blue-tinted city skyline at dusk"></div>
  <div class="brand">HARBORLINE</div>
  <div class="ring" style="width:150px;height:150px;left:-50px;bottom:-70px;border-width:20px"></div>
  <div class="cover-title h" style="right:14px;top:152px">Lorem ipsum dolor sit amet<br>consectetuer adipiscing elit</div>
</section>

<section class="slide cover" style="background:linear-gradient(110deg,#2a5893 40%,#4f8fa3 85%,#6db5a6)">
  <div class="abs photo-city" style="inset:0" role="img" aria-label="City skyline at dusk with teal light"></div>
  <div class="brand">HARBORLINE</div>
  <div class="ring" style="width:150px;height:150px;left:-50px;bottom:-70px;border-width:20px"></div>
  <div class="cover-title h" style="right:14px;top:151px">Lorem ipsum dolor sit amet<br>consectetuer adipiscing elit</div>
</section>

<section class="slide cover">
  <div class="abs photo-city" style="inset:0" role="img" aria-label="City skyline at night, blue tint"></div>
  <div class="brand">HARBORLINE</div>
  <div class="band" style="background:linear-gradient(90deg,#1e3d5e,#2a5e6e)" role="img" aria-label="Night skyline seen through a dark band"></div>
  <div class="ring" style="width:66px;height:66px;left:30px;top:73px;border-width:9px"></div>
  <div class="cover-title h" style="left:100px;top:91px;text-align:left">Lorem ipsum dolor sit amet<br>consectetuer adipiscing elit</div>
</section>

<section class="slide cover">
  <div class="abs photo-city" style="inset:0" role="img" aria-label="City skyline at night, blue tint"></div>
  <div class="brand">HARBORLINE</div>
  <div class="band" style="background:linear-gradient(90deg,#3f7f86,#6db5a6)"></div>
  <div class="ring" style="width:66px;height:66px;left:30px;top:73px;border-width:9px"></div>
  <div class="cover-title h" style="left:100px;top:91px;text-align:left">Lorem ipsum dolor sit amet<br>consectetuer adipiscing elit</div>
</section>

<section class="slide">
  <div class="title h" style="left:85px;top:24px">Welcome Message</div>
  <div class="abs" style="left:0;right:0;top:53px;height:94px;background:linear-gradient(90deg,#2a5a8a,#225079)"></div>
  <div class="ring" style="width:56px;height:56px;left:-14px;top:102px;border-width:7px"></div>
  <p class="abs body" style="left:56px;width:196px;top:84px;color:#fff;text-align:center">Lorem ipsum dolor sit amet, consectetur adipiscing elit, sed do eiusmod tempor incididunt ut labore et dolore magna aliqua. Ut enim ad minim veniam, quis nostrud exercitation ullamco laboris nisi ut aliquip ex ea commodo consequat.</p>
  <div class="foot"><span style="padding-left:2px">www.harborlinegroup.com</span><span class="foot-page">5</span></div>
</section>

<section class="slide">
  <div class="abs" style="left:0;right:0;top:29px;bottom:12px;background:var(--blue)"></div>
  <div class="abs photo-city" style="left:0;right:0;top:29px;bottom:12px" role="img" aria-label="Faint city skyline"></div>
  <div class="ring" style="width:56px;height:56px;left:2px;top:132px;border-width:7px"></div>
  <div class="h abs" style="left:0;right:0;top:62px;text-align:center;color:#fff;font-size:8.5px">Welcome Message</div>
  <p class="abs body" style="left:54px;width:176px;top:94px;color:#fff;text-align:center">Lorem ipsum dolor sit amet, consectetur adipiscing elit, sed do eiusmod tempor incididunt ut labore et dolore magna aliqua. Ut enim ad minim veniam, quis nostrud exercitation ullamco laboris nisi ut aliquip ex ea commodo consequat.</p>
  <div class="foot"><span style="padding-left:2px">www.harborlinegroup.com</span><span class="foot-page">6</span></div>
</section>

<section class="slide">
  <div class="title h">Table of Content</div>
  <div class="toc-item" style="left:26px;top:53px"><span class="toc-num" style="color:var(--ink)">1</span><span class="lbl"><span style="color:var(--ink)">LOREM IPSUM</span><br>Lorem ipsum dolor sit amet,<br>consectetur adipiscing elit</span></div>
  <div class="toc-item" style="left:26px;top:95px"><span class="toc-num" style="color:var(--ink)">2</span><span class="lbl"><span style="color:var(--ink)">LOREM IPSUM</span><br>Lorem ipsum dolor sit amet,<br>consectetur adipiscing elit</span></div>
  <div class="toc-item" style="left:26px;top:137px"><span class="toc-num" style="color:var(--ink)">3</span><span class="lbl"><span style="color:var(--ink)">LOREM IPSUM</span><br>Lorem ipsum dolor sit amet,<br>consectetur adipiscing elit</span></div>
  <div class="toc-item" style="left:146px;top:53px"><span class="toc-num" style="color:var(--orange)">4</span><span class="lbl"><span style="color:var(--orange)">LOREM IPSUM</span><br>Lorem ipsum dolor sit amet,<br>consectetur adipiscing elit</span></div>
  <div class="toc-item" style="left:146px;top:95px"><span class="toc-num" style="color:var(--orange)">5</span><span class="lbl"><span style="color:var(--orange)">LOREM IPSUM</span><br>Lorem ipsum dolor sit amet,<br>consectetur adipiscing elit</span></div>
  <div class="toc-item" style="left:146px;top:137px"><span class="toc-num" style="color:var(--orange)">6</span><span class="lbl"><span style="color:var(--orange)">LOREM IPSUM</span><br>Lorem ipsum dolor sit amet,<br>consectetur adipiscing elit</span></div>
  <div class="foot"><span class="foot-brand">HARBORLINE</span><span>www.harborlinegroup.com</span><span class="foot-page">7</span></div>
</section>

<section class="slide">
  <div class="title h">About Us</div>
  <div class="abs photo-room-blue" style="left:0;right:0;top:30px;height:96px" role="img" aria-label="Empty boardroom with city windows, blue tone"></div>
  <p class="abs body" style="left:14px;top:140px;width:118px">Lorem ipsum dolor sit amet, consectetuer adipiscing elit, sed diam nonummy nibh euismod tincidunt ut laoreet dolore magna aliquam erat volutpat</p>
  <div class="dot" style="left:160px;top:140px;width:19px;height:19px;background:var(--blue)"><svg viewBox="0 0 10 10"><circle cx="3.5" cy="4" r="2" fill="#fff"/><circle cx="6.5" cy="4" r="2" fill="#fff"/><rect x="2" y="6.5" width="6" height="2" fill="#fff"/></svg></div>
  <div class="dot" style="left:200px;top:140px;width:19px;height:19px;background:var(--blue)"><svg viewBox="0 0 10 10"><rect x="1.5" y="3" width="7" height="5" rx=".6" fill="#fff"/><rect x="3.5" y="1.8" width="3" height="1.6" fill="none" stroke="#fff" stroke-width=".8"/></svg></div>
  <div class="dot" style="left:240px;top:140px;width:19px;height:19px;background:var(--blue)"><svg viewBox="0 0 10 10"><rect x="4" y="1" width="2" height="2" fill="#fff"/><rect x="1" y="6.5" width="2" height="2" fill="#fff"/><rect x="4" y="6.5" width="2" height="2" fill="#fff"/><rect x="7" y="6.5" width="2" height="2" fill="#fff"/><path d="M5 3v2M2 6.5V5h6v1.5" stroke="#fff" stroke-width=".6" fill="none"/></svg></div>
  <div class="foot"><span class="foot-brand">HARBORLINE</span><span>www.harborlinegroup.com</span><span class="foot-page">8</span></div>
</section>

<section class="slide">
  <div class="title h">About Us</div>
  <div class="abs photo-room-warm" style="left:0;right:0;top:30px;height:80px" role="img" aria-label="Bright boardroom with leather chairs"></div>
  <div class="dot" style="left:83px;top:102px;width:17px;height:17px;background:var(--blue)"><svg viewBox="0 0 10 10"><circle cx="3.5" cy="4" r="2" fill="#fff"/><circle cx="6.5" cy="4" r="2" fill="#fff"/><rect x="2" y="6.5" width="6" height="2" fill="#fff"/></svg></div>
  <div class="dot" style="left:131px;top:102px;width:17px;height:17px;background:var(--blue)"><svg viewBox="0 0 10 10"><rect x="1.5" y="3" width="7" height="5" rx=".6" fill="#fff"/></svg></div>
  <div class="dot" style="left:180px;top:102px;width:17px;height:17px;background:var(--blue)"><svg viewBox="0 0 10 10"><rect x="4" y="1" width="2" height="2" fill="#fff"/><rect x="1" y="6.5" width="2" height="2" fill="#fff"/><rect x="4" y="6.5" width="2" height="2" fill="#fff"/><rect x="7" y="6.5" width="2" height="2" fill="#fff"/></svg></div>
  <p class="abs body" style="left:70px;width:140px;top:145px;text-align:center">Lorem ipsum dolor sit amet, consectetuer adipiscing elit, sed diam nonummy nibh euismod tincidunt ut laoreet dolore magna aliquam erat volutpat</p>
  <div class="foot"><span class="foot-brand">HARBORLINE</span><span>www.harborlinegroup.com</span><span class="foot-page">9</span></div>
</section>

<section class="slide" style="background:var(--blue)">
  <div class="abs photo-city" style="inset:0" role="img" aria-label="Faint city skyline"></div>
  <div class="ring" style="width:120px;height:120px;left:-34px;top:124px;border-width:17px;border-color:rgba(255,255,255,.35)"></div>
  <div class="h abs" style="left:60px;top:74px;color:#fff;font-size:8.5px">Balancing Agility and Tradition</div>
  <p class="abs body" style="left:60px;top:95px;width:170px;color:#fff">Our solutions team is made up of experts in fields ranging from finance to branding to psychology to sales, ensuring we can provide the very best and most tailored service possible to our diverse client base.</p>
  <div class="foot-sign">HARBORLINE<span class="pill" style="background:var(--orange)">10</span></div>
</section>

<section class="slide" style="background:var(--teal)">
  <div class="abs photo-city" style="inset:0" role="img" aria-label="Faint city skyline"></div>
  <div class="ring" style="width:120px;height:120px;left:-34px;top:124px;border-width:17px;border-color:rgba(255,255,255,.35)"></div>
  <div class="h abs" style="left:60px;top:74px;color:var(--ink);font-size:8.5px">Balancing Agility and Tradition</div>
  <p class="abs body" style="left:60px;top:95px;width:170px;color:var(--ink)">Our solutions team is made up of experts in fields ranging from finance to branding to psychology to sales, ensuring we can provide the very best and most tailored service possible to our diverse client base.</p>
  <div class="foot-sign">HARBORLINE<span class="pill">11</span></div>
</section>

<section class="slide" style="background:var(--lavender)">
  <div class="ring" style="width:120px;height:120px;left:-34px;top:124px;border-width:17px;border-color:rgba(130,150,190,.45)"></div>
  <div class="h abs" style="left:34px;top:66px;color:var(--ink);font-size:14px">&ldquo;</div>
  <div class="h abs" style="left:70px;top:78px;color:var(--ink);font-size:8.3px;line-height:1.55">Your organization is only<br>as good as your people.<br><span style="display:inline-block;margin-top:6px">How good are your people?</span></div>
  <div class="h abs" style="left:229px;top:107px;color:var(--ink);font-size:14px">&rdquo;</div>
  <div class="foot-sign" style="color:var(--ink)">HARBORLINE<span class="pill" style="color:#fff">12</span></div>
</section>

<section class="slide" style="background:var(--orange)">
  <div class="ring" style="width:120px;height:120px;left:-34px;top:124px;border-width:17px;border-color:rgba(255,255,255,.35)"></div>
  <div class="h abs" style="left:54px;top:66px;color:var(--ink);font-size:14px">&ldquo;</div>
  <div class="h abs" style="left:70px;top:78px;color:var(--ink);font-size:8.3px;line-height:1.55">Your organization is only<br>as good as your people.<br><span style="display:inline-block;margin-top:6px">How good are your people?</span></div>
  <div class="h abs" style="left:225px;top:107px;color:var(--ink);font-size:14px">&rdquo;</div>
  <div class="foot-sign">HARBORLINE<span class="pill">13</span></div>
</section>

<section class="slide" style="background:var(--blue)">
  <div class="title h" style="color:var(--orange)">Our Services</div>
  <div class="svc" style="left:26px;top:48px;color:#fff"><span class="ic" style="background:var(--orange)"><svg viewBox="0 0 10 10"><rect x="1" y="1.5" width="8" height="5.5" fill="none" stroke="#fff"/><rect x="4" y="7" width="2" height="1.5" fill="#fff"/></svg></span><div><div class="nm" style="color:var(--orange)">IT Leadership</div><div class="ds">We specialize in developing strong technical leaders into strong business leaders through our 7-month program</div></div></div>
  <div class="svc" style="left:146px;top:48px;color:#fff"><span class="ic" style="background:var(--orange)"><svg viewBox="0 0 10 10"><rect x="1" y="1.5" width="8" height="7" fill="none" stroke="#fff"/><path d="M3 7V5M5 7V3.5M7 7V4.5" stroke="#fff"/></svg></span><div><div class="nm" style="color:var(--orange)">Style Profile Certification</div><div class="ds">Learn how one deals with problems, routine and pace, and how to deal with other people from the company that developed the Harborline Style Profile</div></div></div>
  <div class="svc" style="left:26px;top:105px;color:#fff"><span class="ic" style="background:var(--orange)"><svg viewBox="0 0 10 10"><rect x="1.5" y="4" width="7" height="5" fill="none" stroke="#fff"/><path d="M1 4L5 1.5 9 4" stroke="#fff" fill="none"/></svg></span><div><div class="nm" style="color:var(--orange)">Harborline Management School</div><div class="ds">We fast track new managers on a development path through skill-building exercises led by professional managers over this one-month intensive experience</div></div></div>
  <div class="svc" style="left:146px;top:105px;color:#fff"><span class="ic" style="background:var(--orange)"><svg viewBox="0 0 10 10"><path d="M1 5l3-2 2 1 3-1M2 6l2 2 2-1 2-2" stroke="#fff" fill="none"/></svg></span><div><div class="nm" style="color:var(--orange)">Supplier Insight Review</div><div class="ds">Get a full report with measured summaries and next steps concerning success factors of accountability, trust, quality, transparency, communication, and more.</div></div></div>
  <div class="foot" style="background:#fff;color:var(--ink)"><span class="foot-brand" style="color:var(--ink)">HARBORLINE</span><span>www.harborlinegroup.com</span><span class="foot-page" style="color:#fff">14</span></div>
</section>

<section class="slide">
  <div class="title h">Our Services</div>
  <div class="svc" style="left:26px;top:48px"><span class="ic" style="border:.8px solid var(--ink)"><svg viewBox="0 0 10 10"><rect x="1" y="1.5" width="8" height="5.5" fill="none" stroke="#2a4f80"/></svg></span><div><div class="nm" style="color:var(--ink)">IT Leadership</div><div class="ds">We specialize in developing strong technical leaders into strong business leaders through our 7-month program</div></div></div>
  <div class="svc" style="left:146px;top:48px"><span class="ic" style="border:.8px solid var(--ink)"><svg viewBox="0 0 10 10"><path d="M3 7V5M5 7V3.5M7 7V4.5" stroke="#2a4f80"/></svg></span><div><div class="nm" style="color:var(--ink)">Style Profile Certification</div><div class="ds">Learn how one deals with problems, routine and pace, and how to deal with other people from the company that developed the Harborline Style Profile</div></div></div>
  <div class="svc" style="left:26px;top:105px"><span class="ic" style="border:.8px solid var(--ink)"><svg viewBox="0 0 10 10"><rect x="1.5" y="4" width="7" height="5" fill="none" stroke="#2a4f80"/></svg></span><div><div class="nm" style="color:var(--ink)">Harborline Management School</div><div class="ds">We fast track new managers on a development path through skill-building exercises led by professional managers over this one-month intensive experience</div></div></div>
  <div class="svc" style="left:146px;top:105px"><span class="ic" style="border:.8px solid var(--ink)"><svg viewBox="0 0 10 10"><path d="M1 5l3-2 2 1 3-1M2 6l2 2 2-1 2-2" stroke="#2a4f80" fill="none"/></svg></span><div><div class="nm" style="color:var(--ink)">Supplier Insight Review</div><div class="ds">Get a full report with measured summaries and next steps concerning success factors of accountability, trust, quality, transparency, communication, and more.</div></div></div>
  <div class="foot"><span class="foot-brand">HARBORLINE</span><span>www.harborlinegroup.com</span><span class="foot-page">15</span></div>
</section>

<section class="slide">
  <div class="title h">Our Services</div>
  <div class="abs" style="left:94px;top:50px;width:88px;height:88px;border-radius:50%;background:conic-gradient(var(--orange) 0 25%,var(--navy) 0 50%,var(--teal) 0 75%,var(--blue) 0)" role="img" aria-label="Four-part services wheel"></div>
  <div class="abs" style="left:124px;top:80px;width:28px;height:28px;border-radius:50%;background:#fff"></div>
  <div class="abs" style="left:131px;top:87px;width:14px;height:14px;border-radius:50%;background:var(--blue)"></div>
  <div class="abs" style="left:14px;top:64px;width:74px;text-align:right;font-size:3.9px;line-height:1.5"><div style="font-size:5.2px;color:var(--ink)">IT Leadership</div>We specialize in developing strong technical leaders into strong business leaders through our 7-month program</div>
  <div class="abs" style="left:12px;top:122px;width:76px;text-align:right;font-size:3.9px;line-height:1.5"><div style="font-size:5.2px;color:var(--teal)">Harborline<br>Management School</div>We fast track new managers on a development path through skill-building exercises led by professional managers over this one-month intensive experience</div>
  <div class="abs" style="left:190px;top:64px;width:80px;font-size:3.9px;line-height:1.5"><div style="font-size:5.2px;color:var(--orange)">Style Profile Certification</div>Learn how one deals with problems, routine and pace, and how to deal with other people from the company that developed the Harborline Style Profile</div>
  <div class="abs" style="left:190px;top:122px;width:80px;font-size:3.9px;line-height:1.5"><div style="font-size:5.2px;color:var(--navy)">Supplier<br>Insight Review</div>Get a full report with measured summaries and next steps concerning success factors of accountability, trust, quality, transparency, communication, and more.</div>
  <div class="foot"><span class="foot-brand">HARBORLINE</span><span>www.harborlinegroup.com</span><span class="foot-page">16</span></div>
</section>

<section class="slide">
  <div class="title h">Our Services</div>
  <div class="card" style="left:34px;top:34px" role="img" aria-label="Faded office photo behind service card"><div class="nm">IT Leadership</div>We specialize in developing strong technical leaders into strong business leaders through our 7-month program</div>
  <div class="card" style="left:147px;top:34px" role="img" aria-label="Faded office photo behind service card"><div class="nm">Style Profile Certification</div>Learn how one deals with problems, routine and pace, and how to deal with other people from the company</div>
  <div class="card" style="left:34px;top:108px" role="img" aria-label="Faded office photo behind service card"><div class="nm">Harborline Management School</div>We fast track new managers on a development path through skill-building exercises led by professional managers</div>
  <div class="card" style="left:147px;top:108px" role="img" aria-label="Faded office photo behind service card"><div class="nm">Supplier Insight Review</div>Get a full report with measured summaries and next steps concerning success factors of accountability, trust, quality, transparency, communication, and more.</div>
  <div class="foot"><span class="foot-brand">HARBORLINE</span><span>www.harborlinegroup.com</span><span class="foot-page">17</span></div>
</section>

<section class="slide diff">
  <div class="title h">The Harborline Difference</div>
  <div class="abs" style="left:28px;top:42px;width:110px">
    <div class="k">Heart-led, data-driven</div><div class="ds">While our offerings are rooted in proven diagnostic and theoretical principles, they are built around the practical and applicable needs of the ever-adjusting business landscape.</div>
    <div class="k">Job-focused</div><div class="ds">Most other instruments are superficial, classifying all people into a few broad categories. At Harborline, we know better and utilize a range of simple instruments.</div>
    <div class="k">Scalable &amp; enduring</div><div class="ds">Our clients remain loyal over long periods of time because they recognize that our tools, products, and services help reduce cost as they improve revenue.</div>
  </div>
  <div class="circle" style="left:148px;top:52px;width:64px;height:64px;background:var(--teal)"></div>
  <div class="circle" style="left:200px;top:52px;width:64px;height:64px;background:var(--orange)"></div>
  <div class="circle" style="left:176px;top:82px;width:64px;height:64px;background:var(--blue);opacity:.92"></div>
  <div class="foot"><span class="foot-brand">HARBORLINE</span><span>www.harborlinegroup.com</span><span class="foot-page">18</span></div>
</section>

<section class="slide diff">
  <div class="title h">The Harborline Difference</div>
  <div class="abs" style="left:28px;top:42px;width:110px">
    <div class="k">Heart-led, data-driven</div><div class="ds">While our offerings are rooted in proven diagnostic and theoretical principles, they are built around the practical and applicable needs of the ever-adjusting business landscape.</div>
    <div class="k">Job-focused</div><div class="ds">Most other instruments are superficial, classifying all people into a few broad categories. At Harborline, we know better and utilize a range of simple instruments.</div>
    <div class="k">Scalable &amp; enduring</div><div class="ds">Our clients remain loyal over long periods of time because they recognize that our tools, products, and services help reduce cost as they improve revenue.</div>
  </div>
  <div class="circle" style="left:147px;top:70px;width:72px;height:72px;background:var(--teal)"></div>
  <div class="circle" style="left:191px;top:70px;width:72px;height:72px;background:var(--orange)"></div>
  <div class="circle" style="left:167px;top:34px;width:72px;height:72px;background:var(--blue)"></div>
  <div class="abs" style="left:193px;top:72px;width:20px;height:20px;border-radius:50%;background:#fff;border:2px solid var(--blue)"></div>
  <div class="foot"><span class="foot-brand">HARBORLINE</span><span>www.harborlinegroup.com</span><span class="foot-page">19</span></div>
</section>

<section class="slide diff">
  <div class="title h">The Harborline Difference</div>
  <div class="dot" style="left:37px;top:46px;width:22px;height:22px;background:var(--teal)"><svg viewBox="0 0 10 10"><path d="M3 8V6M5 8V3M7 8V5" stroke="#fff" stroke-width="1.2"/></svg></div>
  <div class="abs" style="left:70px;top:46px;width:180px"><div class="k" style="color:var(--teal)">Heart-led, data-driven</div><div class="ds">While our offerings are rooted in proven diagnostic and theoretical principles, they are built around the practical and applicable needs of the ever-adjusting business landscape.</div></div>
  <div class="dot" style="left:37px;top:90px;width:22px;height:22px;background:var(--blue)"><svg viewBox="0 0 10 10"><circle cx="5" cy="5" r="3" fill="#fff"/></svg></div>
  <div class="abs" style="left:70px;top:90px;width:180px"><div class="k" style="color:var(--ink)">Scalable &amp; enduring</div><div class="ds">Our clients remain loyal over long periods of time because they recognize that our tools, products, and services help reduce cost as they improve revenue.</div></div>
  <div class="dot" style="left:37px;top:134px;width:22px;height:22px;background:var(--orange)"><svg viewBox="0 0 10 10"><circle cx="5" cy="4" r="2" fill="#fff"/><rect x="2.5" y="6.5" width="5" height="2" fill="#fff"/></svg></div>
  <div class="abs" style="left:70px;top:134px;width:180px"><div class="k">Job-focused</div><div class="ds">Most other instruments are superficial, classifying all people into a few broad categories. At Harborline, we know better and utilize a range of instruments.</div></div>
  <div class="foot"><span class="foot-brand">HARBORLINE</span><span>www.harborlinegroup.com</span><span class="foot-page">20</span></div>
</section>

</main>
</body>
</html>
```